Vice chair

I'm running for a position as vice chair this will be posted in the lunch room cafeteria in this package i posted logos, my picture, sample of old flyers to give you a idea i also wrote literature need help in putting it together like it to look like a million bucks goal win this election I summited lots of pdf files and jpeg look though them to help with your design feel free to contact me to further assist you
Updates

Would like this to be completed by Wednesday

Target Market(s)

My constituents

Font styles to use
Serif

Colors

Designer to choose colors to be used in the design.

Requirements
Must have
• Make it look clean neat
Nice to have
• Nice background

```html
<!DOCTYPE html>
<html lang="en">
<head>
<meta charset="utf-8">
<title>Elect Marco Delgado – Vice Chair</title>
<link rel="stylesheet" href="https://fonts.googleapis.com/css2?family=Playfair+Display:wght@700;900&family=Raleway:ital,wght@0,400;0,600;0,700;1,500&display=swap">
<style>
  :root{
    --backdrop:#8c9191;
    --navy:#1f3f9e;
    --blue:#2b5bd7;
    --blue-light:#4f86f0;
    --red:#e0242c;
    --white:#ffffff;
    --ink:#2a2a2a;
    --silver:#dfe5ef;
    --slate-box:#c9d3e6;
  }
  *{box-sizing:border-box;margin:0;padding:0}
  html,body{width:938px;height:1200px;overflow:hidden}
  body{background:var(--backdrop);font-family:"Raleway",sans-serif;color:var(--ink)}
  .flyer{position:absolute;left:41px;top:34px;width:856px;height:1133px;background:var(--white);overflow:hidden}
  .header{position:absolute;inset:0 0 auto 0;height:470px}
  .header svg{position:absolute;inset:0}
  .stars{position:absolute;left:150px;top:30px;display:flex;gap:20px}
  .stars svg{width:32px;height:32px}
  .stars svg:nth-child(1),.stars svg:nth-child(5){margin-top:20px}
  .stars svg:nth-child(2),.stars svg:nth-child(4){margin-top:6px}
  .headline{position:absolute;left:40px;top:82px;width:440px;text-align:center;color:var(--white);font-family:"Playfair Display",serif;line-height:1}
  .headline .elect{font-size:48px;font-weight:700}
  .headline .first{font-size:98px;font-weight:900;letter-spacing:1px;margin-top:4px;color:var(--silver)}
  .headline .last{font-size:54px;font-weight:900;letter-spacing:3px;margin-top:4px;color:var(--silver)}
  .headline .role{font-family:"Raleway",sans-serif;font-size:24px;font-weight:600;margin-top:16px;letter-spacing:.5px}
  .portrait{position:absolute;left:494px;top:50px;width:240px;height:265px;background:linear-gradient(160deg,#6b5a50,#3a3230 60%,#2a2c3a)}
  .seal{position:absolute;left:494px;top:380px;width:226px;height:226px}
  .seal-text{position:absolute;left:519px;top:425px;width:176px;text-align:center;color:var(--white)}
  .seal-text h2{font-family:"Playfair Display",serif;font-size:27px;line-height:1.1;font-weight:700}
  .seal-text p{font-size:12.5px;line-height:1.3;font-weight:600;margin-top:10px}
  .badge{position:absolute;width:124px;height:124px;border-radius:50%}
  .badge.elm{left:50px;top:557px;background:#f2c21a;border:5px solid #b3242a}
  .badge.fields{left:182px;top:542px;background:#dbe4f7;border:5px solid var(--blue)}
  .badge.stone{left:309px;top:542px;background:#f08a2a;border:5px solid #6e6f71}
  .intro{position:absolute;left:62px;top:712px;width:392px;font-size:14px;line-height:1.36}
  .intro p+p{margin-top:14px}
  .intro .ask{color:var(--blue)}
  .facts{position:absolute;left:478px;top:612px;width:330px;list-style:none;font-size:14.5px;line-height:1.35}
  .facts li{display:flex;gap:14px;margin-bottom:16px}
  .facts svg{flex:none;width:22px;height:22px;margin-top:1px}
  .closing{position:absolute;left:478px;top:838px;width:378px;height:176px;background:var(--blue);color:var(--white);padding:16px 36px 0 18px;font-style:italic;font-weight:500;font-size:14.5px;line-height:1.35}
  .pledge{position:absolute;left:478px;top:1026px;width:360px;font-family:"Playfair Display",serif;font-weight:700;font-size:27px;line-height:1.2;color:var(--navy)}
  .slate-name{position:absolute;left:60px;top:1042px;display:flex;align-items:center;gap:10px;font-weight:700;font-size:18px;color:#6aa632}
  .slate-name .dot{width:28px;height:28px;border-radius:50%;background:#f2b51a}
  .vote{position:absolute;left:234px;top:1024px;display:flex;align-items:center;width:222px;height:66px;background:var(--slate-box);border-radius:4px}
  .vote svg{width:66px;height:66px;flex:none}
  .vote span{font-family:"Playfair Display",serif;font-weight:700;font-size:22px;line-height:1.05;color:var(--navy);padding-left:12px}
  .footer-band{position:absolute;left:0;right:0;bottom:0;height:22px;background:linear-gradient(var(--red) 0 45%,var(--white) 45% 55%,var(--navy) 55%)}
</style>
</head>
<body>
<div class="flyer">
  <div class="header">
    <svg viewBox="0 0 856 470" width="856" height="470" aria-hidden="true">
      <defs>
        <radialGradient id="skyGlow" cx="0.3" cy="0.35" r="0.8">
          <stop offset="0" stop-color="var(--blue-light)"/>
          <stop offset="1" stop-color="var(--navy)"/>
        </radialGradient>
      </defs>
      <path d="M0 0H856V380C640 420 420 350 0 430Z" fill="url(#skyGlow)"/>
      <path d="M0 450C420 370 640 440 856 400" fill="none" stroke="var(--red)" stroke-width="22"/>
      <path d="M0 472C420 392 640 462 856 422" fill="none" stroke="var(--navy)" stroke-width="8"/>
    </svg>
  </div>

  <div class="stars" aria-hidden="true">
    <svg viewBox="0 0 24 24"><path d="M12 2l2.9 6.6 7.1.6-5.4 4.7 1.6 7-6.2-3.7-6.2 3.7 1.6-7L2 9.2l7.1-.6z" fill="#fff"/></svg>
    <svg viewBox="0 0 24 24"><path d="M12 2l2.9 6.6 7.1.6-5.4 4.7 1.6 7-6.2-3.7-6.2 3.7 1.6-7L2 9.2l7.1-.6z" fill="#fff"/></svg>
    <svg viewBox="0 0 24 24"><path d="M12 2l2.9 6.6 7.1.6-5.4 4.7 1.6 7-6.2-3.7-6.2 3.7 1.6-7L2 9.2l7.1-.6z" fill="#fff"/></svg>
    <svg viewBox="0 0 24 24"><path d="M12 2l2.9 6.6 7.1.6-5.4 4.7 1.6 7-6.2-3.7-6.2 3.7 1.6-7L2 9.2l7.1-.6z" fill="#fff"/></svg>
    <svg viewBox="0 0 24 24"><path d="M12 2l2.9 6.6 7.1.6-5.4 4.7 1.6 7-6.2-3.7-6.2 3.7 1.6-7L2 9.2l7.1-.6z" fill="#fff"/></svg>
  </div>

  <h1 class="headline">
    <div class="elect">Elect</div>
    <div class="first">MARCO</div>
    <div class="last">DELGADO</div>
    <div class="role">AS YOUR VICE CHAIR A PERSON</div>
  </h1>

  <div class="portrait" role="img" aria-label="Portrait photo of the candidate"></div>

  <svg class="seal" viewBox="0 0 262 262" aria-hidden="true">
    <circle cx="131" cy="131" r="131" fill="var(--red)"/>
    <circle cx="131" cy="131" r="116" fill="none" stroke="#fff" stroke-width="5" stroke-dasharray="1 11" stroke-linecap="round"/>
  </svg>
  <div class="seal-text">
    <h2>Respect &amp; Integrity</h2>
    <p>Transit Workers Alliance will be the BACKBONE THATS SHAPES OUR UNION</p>
  </div>

  <div class="badge elm" role="img" aria-label="Elm Ridge Depot badge"></div>
  <div class="badge fields" role="img" aria-label="North Fields Depot badge"></div>
  <div class="badge stone" role="img" aria-label="Stonebrook Depot badge"></div>

  <div class="intro">
    <p>I Marco Delgado for those who don't know me would like to introduce myself I have always been approachable and helpful whether you are a probationary officer or a veteran operator with knowledge or information. We must protect our union rules for ourselves our future and most important our children.</p>
    <p>I would like this opportunity to run as your vice chair a person you can trust and believe in me Positive and motivations are my main keys for progress and for change in my campaign When there are no leaders to look up to one therefore must become one</p>
    <p>I do believe I'm the right person for this positio so <span class="ask">please come out and support me and vote me as YOUR VICE CHAIR</span></p>
  </div>

  <ul class="facts">
    <li><svg viewBox="0 0 22 22"><rect width="22" height="22" fill="var(--navy)"/><path d="M11 4l2 4.4 4.7.4-3.6 3.1 1.1 4.6-4.2-2.5-4.2 2.5 1.1-4.6-3.6-3.1 4.7-.4z" fill="#fff"/></svg><span>20 years on the job</span></li>
    <li><svg viewBox="0 0 22 22"><rect width="22" height="22" fill="var(--navy)"/><path d="M11 4l2 4.4 4.7.4-3.6 3.1 1.1 4.6-4.2-2.5-4.2 2.5 1.1-4.6-3.6-3.1 4.7-.4z" fill="#fff"/></svg><span>Past union member of Carriers local 214 belives in There is a collective bargaining agreement in place and no management is above the law to violate it</span></li>
    <li><svg viewBox="0 0 22 22"><rect width="22" height="22" fill="var(--navy)"/><path d="M11 4l2 4.4 4.7.4-3.6 3.1 1.1 4.6-4.2-2.5-4.2 2.5 1.1-4.6-3.6-3.1 4.7-.4z" fill="#fff"/></svg><span>Past union member of Carriers local 736 believes a house that is divided cannot stand alone</span></li>
  </ul>

  <div class="closing">In closing I believe that our union does not stand out individually achievement we must stand for collective advancement for all, we must always continue to stand together, stay together &amp; fight together so we can win together because success is never owned, it is rented and the rent is due every day.</div>

  <div class="pledge">Vote independent me as your vice chair</div>

  <div class="slate-name"><span class="dot"></span>New Direction</div>

  <div class="vote">
    <svg viewBox="0 0 68 68" aria-hidden="true"><rect width="68" height="68" rx="4" fill="var(--blue)"/><path d="M20 20L48 48M48 20L20 48" stroke="#fff" stroke-width="8" stroke-linecap="round"/></svg>
    <span>Vote for<br>the Slate</span>
  </div>

  <div class="footer-band"></div>
</div>
</body>
</html>
```